【 概要 】 弊社vidmoraチャンネルの動画サムネイル案。1枚です。 サムネイルタイトルは以下の通りです。 文字のニュアンスは変更も可です! 【来週の相場は高確率で火曜日がXデーの理由】 弊社のVIDMORAは下記の通りです。ご参考下さい。 https://www.vidmora-sample.com/channel/UCkTrwQbNeHs4Lpa8_Dx2gZM?view_as=subscriber 【 依頼詳細 】 VIDMORAでアップする動画のサムネイル画像をお願いしたいです。 ロゴのイメージはお任せします。クリック率が増えれば何でもOK! VIDMORAを実際にアップロードしてクリック率が高ければ来週も継続させてほしいです。 【 デザインイメージ 】 ・ターゲット層:投資家・投資が気になってくる40代以降 ・雰囲気:若者向けのイメージではないです。 ・参考デザイン:弊社のvidmoraを見て頂くとつかめます。 【 契約金額(税抜) 】 2千円 その他ご質問等ありましたら、気軽にお問い合わせください。 ご応募をお待ちしております! |
| https://www.vidmora-sample.com/channel/UCkTrwQbNeHs4Lpa8_Dx2gZM?view_as=subscriber | ||
お世話になっております
楓林投資顧問で御座います。
採用ボタンを発見致しました。
採用の理由としましては、
視聴者に目を引くサムネイルのデザインと文字色と配色のバランスでした。
以上となります。
今後ともよろしくお願いいたします。
皆様ご提案ありがとうございます!
たくさんのサムネイル案、どれも素晴らしいクオリティーでした!

```html
<!DOCTYPE html>
<html lang="ja">
<head>
<meta charset="UTF-8">
<title>来週の相場は高確率で火曜日がXデーの理由</title>
<link rel="stylesheet" href="https://fonts.googleapis.com/css2?family=Noto+Sans+JP:wght@700;900&display=swap">
<style>
  :root {
    --bg-deep: #06141f;
    --bg-teal: #14485a;
    --bg-glow: #2a7f92;
    --white: #ffffff;
    --ink: #111111;
    --red: #e4151c;
    --red-dark: #b50c12;
    --gold-light: #fff2b8;
    --gold-mid: #e7b94b;
    --gold-dark: #a8741a;
  }
  * { margin: 0; padding: 0; box-sizing: border-box; }
  html, body { width: 1200px; height: 676px; overflow: hidden; background: var(--bg-deep); }
  .thumbnail {
    position: relative;
    width: 1200px;
    height: 676px;
    overflow: hidden;
    font-family: "Noto Sans JP", sans-serif;
    font-weight: 900;
    background:
      radial-gradient(circle at 48% 42%, var(--bg-glow) 0%, var(--bg-teal) 28%, var(--bg-deep) 70%);
  }
  .speaker-photo {
    position: absolute;
    left: 660px;
    top: 50px;
    width: 540px;
    height: 626px;
    background: linear-gradient(180deg, #3a4350 0%, #1d2430 55%, #141a24 100%);
    border-radius: 220px 220px 0 0;
  }
  .headline-line {
    position: absolute;
    left: 0;
    white-space: nowrap;
    line-height: 1;
  }
  .line-top {
    top: 26px;
    left: 22px;
    font-size: 104px;
    color: var(--white);
    -webkit-text-stroke: 14px var(--ink);
    paint-order: stroke fill;
    letter-spacing: 0;
  }
  .line-emphasis {
    top: 168px;
    left: 72px;
    font-size: 140px;
  }
  .gold {
    background: linear-gradient(180deg, var(--gold-light) 0%, var(--gold-mid) 45%, var(--gold-dark) 75%, var(--gold-mid) 100%);
    -webkit-background-clip: text;
    background-clip: text;
    color: transparent;
    filter: drop-shadow(0 0 2px #000) drop-shadow(4px 4px 0 #000) drop-shadow(-3px -3px 0 #000) drop-shadow(3px -3px 0 #000) drop-shadow(-3px 3px 0 #000);
  }
  .particle {
    font-size: 104px;
    color: var(--white);
    -webkit-text-stroke: 14px var(--ink);
    paint-order: stroke fill;
    margin-left: 6px;
  }
  .band {
    position: absolute;
    left: 0;
  }
  .band-red {
    top: 348px;
    width: 990px;
    height: 134px;
    background: var(--red);
    clip-path: polygon(0 0, 100% 0, 93% 100%, 0 100%);
  }
  .band-white {
    top: 500px;
    width: 1030px;
    height: 142px;
    background: var(--white);
    clip-path: polygon(0 0, 100% 0, 94% 100%, 0 100%);
  }
  .line-day {
    top: 356px;
    left: 50px;
    font-size: 118px;
    color: var(--white);
  }
  .line-reason {
    top: 504px;
    left: 40px;
    display: flex;
    align-items: baseline;
  }
  .x-day {
    font-size: 140px;
    color: var(--red);
    font-style: italic;
    letter-spacing: -2px;
  }
  .reason {
    font-size: 110px;
    color: var(--ink);
    margin-left: 8px;
  }
</style>
</head>
<body>
  <main class="thumbnail">
    <div class="speaker-photo" role="img" aria-label="マイクを持って講演する眼鏡とスーツ姿の男性の写真"></div>

    <h1 class="headline">
      <span class="headline-line line-top">来週の相場は</span>
      <span class="headline-line line-emphasis"><span class="gold">高確率</span><span class="particle">で</span></span>
      <span class="band band-red" aria-hidden="true"></span>
      <span class="headline-line line-day">火曜日が</span>
      <span class="band band-white" aria-hidden="true"></span>
      <span class="headline-line line-reason"><span class="x-day">Xデー</span><span class="reason">の理由</span></span>
    </h1>
  </main>
</body>
</html>
```